Business Card Design

I am specialising in Designs, Drafting and Council approvals. From the idea to the full set of plans and other documents. Residential houses only.
I am located in Northern Beaches, Sydney where the sky is always blue :)
Tallwood Drafting should be associated with light, modern house designs & with 3D drafting. I am positive person, that would like help every client through the demanding time of council paperwork.

The business card should be light blue, with white 3D sketch and white or black writing. Simple, modern and "happy"

Please don't hesitate to suggest something if you think so.

Thanks
Mirela

Industry/Entity Type

House

Contact Information for Business Card

FRONT:

Tallwood Drafting
Servicing Northern Beaches

Mirela Ostrowe
tallwooddrafting@mailhaven.com.au
0427 586 293
www.tallwooddrafting.com.au

BACK:

Design consultation
Plans Drafting
3D Visualisation
Council Approvals

```html
<!DOCTYPE html>
<html lang="en">
<head>
<meta charset="utf-8">
<title>Tallwood Drafting – Business Card</title>
<link rel="stylesheet" href="https://fonts.googleapis.com/css2?family=Cinzel:wght@500&family=Open+Sans:wght@400;600;700&family=Roboto+Slab:wght@700&display=swap">
<style>
  :root {
    --sky: #1ba3d6;
    --sky-deep: #1577ab;
    --sky-pale: #5cc0e6;
    --paper: #ffffff;
    --ink-teal: #1b5a78;
    --ink-dark: #17323f;
    --plan-grey: #d9dde0;
    --backdrop: #eef1f3;
  }
  * { margin: 0; padding: 0; box-sizing: border-box; }
  html, body {
    width: 1200px; height: 1000px; overflow: hidden;
    background: var(--backdrop);
  }
  .sheet {
    position: relative; width: 1200px; height: 1000px;
    display: flex; flex-direction: column; align-items: center; justify-content: center; gap: 50px;
  }
  .card {
    position: relative; width: 600px; height: 370px;
    border-radius: 22px; overflow: hidden;
    box-shadow: 0 10px 28px rgba(0,0,0,0.18);
  }

  /* Front */
  .card-front { background: var(--paper); }
  .front-top { position: absolute; left: 0; top: 0; width: 100%; height: 195px; }
  .floor-plan {
    position: absolute; left: 0; top: 0; width: 305px; height: 210px;
    background: linear-gradient(135deg, #f4f5f6 0%, var(--plan-grey) 100%);
  }
  .holder-name {
    position: absolute; left: 325px; top: 138px;
    font-family: "Cinzel", serif; font-weight: 500; font-size: 25px;
    color: var(--ink-teal); letter-spacing: 0.5px;
  }
  .front-band {
    position: absolute; left: 0; top: 195px; width: 100%; height: 175px;
    background: var(--sky); text-align: center; color: var(--paper);
    font-family: "Open Sans", sans-serif;
  }
  .brand-name {
    margin-top: 18px;
    font-family: "Roboto Slab", serif; font-weight: 700; font-size: 38px;
    line-height: 1.1; color: var(--paper);
  }
  .contact-email { margin-top: 14px; font-size: 12.5px; font-weight: 700; }
  .contact-phone { font-size: 23px; font-weight: 700; line-height: 1.2; }
  .contact-web { font-size: 18px; font-weight: 400; color: var(--ink-dark); line-height: 1.3; }

  /* Back */
  .card-back { background: var(--sky); }
  .house-sketch {
    position: absolute; inset: 0;
    background: linear-gradient(160deg, var(--sky-pale) 0%, var(--sky) 55%, #1796c8 100%);
  }
  .services-band {
    position: absolute; left: 45px; right: 45px; top: 165px; height: 80px;
    background: var(--sky-deep); opacity: 0.92;
    display: flex; flex-direction: column; align-items: center; justify-content: center;
    color: var(--paper); font-family: "Roboto Slab", serif; font-weight: 700;
  }
  .services-title { font-size: 32px; letter-spacing: 1px; line-height: 1.1; }
  .services-list { font-size: 14px; letter-spacing: 0.6px; word-spacing: 4px; margin-top: 2px; }
</style>
</head>
<body>
  <main class="sheet">
    <section class="card card-front" aria-label="Business card front">
      <div class="front-top">
        <div class="floor-plan" role="img" aria-label="Architectural floor plan drawing of a master bedroom, ensuite and foyer"></div>
        <p class="holder-name">Mirela Ostrowe</p>
      </div>
      <div class="front-band">
        <p class="brand-name">Tallwood Drafting</p>
        <p class="contact-email">Email: tallwooddrafting@mailhaven.com.au</p>
        <p class="contact-phone">Tel: 0427 586 293</p>
        <p class="contact-web">www.tallwooddrafting.com.au</p>
      </div>
    </section>

    <section class="card card-back" aria-label="Business card back">
      <div class="house-sketch" role="img" aria-label="Faint white 3D line sketch of a modern house with an outdoor staircase"></div>
      <div class="services-band">
        <p class="services-title">Design Consultation</p>
        <p class="services-list">Plans Drafting 3D Visualisation Council Approvals</p>
      </div>
    </section>
  </main>
</body>
</html>
```